Young Balance Support Network

We need a poster explaining that some children live with a disability called Vestibular Disorder. Feel free to ask question. We want you to respect our color code, same as our logo.

Here is our website : http://www.ybsnetwork.org/

We need to sensibilise people about this disability for children.

Industry/Entity Type

Charity

Font styles to use
Serif

Requirements
Must have
• 1. our logo (with all our details) + one of the photo of Marek
• 2. design showing a child with a dizziness for exemple
• 3. a title saying : Aidez-nous à changer la vie des enfants vivant avec un problème vestibulaire
• 4.include the text attached (information flyer YBSN)
• Poster size : 24"X 36"
Should not have
• wheel chair

```html
<!DOCTYPE html>
<html lang="en">
<head>
<meta charset="utf-8">
<title>Young Balance Support Network – Flyer</title>
<link rel="stylesheet" href="https://fonts.googleapis.com/css2?family=Fjalla+One&family=Open+Sans:wght@400&family=Ubuntu:wght@300;400&display=swap">
<style>
  :root {
    --brand-blue: #29a8e0;
    --sky-blue: #00aeef;
    --brand-green: #8dc63f;
    --brand-yellow: #ffc915;
    --ink: #4d4d4d;
    --paper: #ffffff;
    --mist: #eef3f8;
    --white: #ffffff;
  }
  * { box-sizing: border-box; margin: 0; padding: 0; }
  html, body { width: 1000px; height: 1200px; overflow: hidden; background: var(--paper); }
  .flyer { position: relative; width: 1000px; height: 1200px; background: var(--paper); overflow: hidden; font-family: "Open Sans", sans-serif; color: var(--ink); }
  .artwork { position: absolute; inset: 0; }
  .brand { position: absolute; left: 52px; top: 60px; }
  .brand-mark { display: flex; align-items: center; gap: 14px; margin-left: 108px; }
  .brand-dot { width: 44px; height: 44px; border-radius: 50%; background: var(--brand-blue); }
  .brand-acronym { font-family: "Ubuntu", sans-serif; font-weight: 400; font-size: 34px; letter-spacing: 3px; color: var(--brand-green); }
  .brand-name { margin-top: 100px; font-family: "Ubuntu", sans-serif; font-weight: 400; font-size: 36px; line-height: 42px; color: var(--brand-blue); }
  .section-title { font-family: "Fjalla One", sans-serif; font-weight: 400; color: var(--brand-green); font-size: 27px; line-height: 1.1; }
  .intro { position: absolute; left: 47px; top: 476px; width: 486px; }
  .intro p { margin-top: 12px; font-size: 18px; line-height: 23.6px; text-align: justify; }
  .consequences { position: absolute; left: 40px; top: 710px; width: 520px; }
  .consequences ul { list-style: none; margin-top: 10px; }
  .consequences li { font-size: 16px; line-height: 27px; padding-left: 12px; text-indent: -10px; }
  .consequences li::before { content: "• "; }
  .compensation { position: absolute; left: 568px; top: 442px; width: 405px; height: 469px; background: var(--brand-blue); border-radius: 0 0 16px 16px; padding: 58px 24px 0 32px; color: var(--white); box-shadow: 0 6px 10px rgba(0,0,0,0.18); }
  .compensation .section-title { color: var(--white); font-size: 27px; line-height: 38px; }
  .compensation p { margin-top: 16px; font-size: 18px; line-height: 24px; text-align: justify; }
  .compensation p + p { margin-top: 24px; }
  .contact { position: absolute; right: 29px; top: 1068px; text-align: right; color: var(--white); font-family: "Open Sans", sans-serif; font-size: 16px; line-height: 28px; }
  .contact .web { font-family: "Ubuntu", sans-serif; font-weight: 300; font-size: 31px; line-height: 44px; margin-top: 2px; }
  .social { position: absolute; left: 410px; top: 1128px; display: flex; align-items: center; gap: 10px; }
  .social-dot { width: 40px; height: 40px; border-radius: 50%; background: var(--brand-green); }
  .social-name { font-family: "Open Sans", sans-serif; font-size: 16px; color: var(--white); }
</style>
</head>
<body>
<main class="flyer">
  <svg class="artwork" viewBox="0 0 1000 1200" width="1000" height="1200" aria-hidden="false">
    <defs>
      <linearGradient id="mist-fade" x1="0" y1="0" x2="0" y2="1">
        <stop offset="0" stop-color="#eef3f8"/>
        <stop offset="1" stop-color="#ffffff"/>
      </linearGradient>
      <linearGradient id="photo-tone" x1="0" y1="0" x2="0" y2="1">
        <stop offset="0" stop-color="#eceef0"/>
        <stop offset="0.55" stop-color="#d9cfd2"/>
        <stop offset="1" stop-color="#5a5a62"/>
      </linearGradient>
      <clipPath id="photo-clip">
        <ellipse cx="800" cy="150" rx="300" ry="300"/>
      </clipPath>
    </defs>

    <!-- soft panel behind the intro text -->
    <rect class="text-backdrop" x="0" y="400" width="570" height="300" fill="url(#mist-fade)"/>

    <!-- child photo area -->
    <g class="photo-frame">
      <rect x="480" y="0" width="520" height="460" fill="url(#photo-tone)" clip-path="url(#photo-clip)" role="img" aria-label="Photo of a smiling toddler with a pink headband, lifted up in the air against a pale sky"/>
      <ellipse cx="800" cy="150" rx="306" ry="306" fill="none" stroke="var(--brand-yellow)" stroke-width="8"/>
      <ellipse cx="800" cy="150" rx="316" ry="316" fill="none" stroke="var(--brand-green)" stroke-width="10"/>
      <rect x="470" y="-10" width="540" height="6" fill="none"/>
    </g>

    <!-- left swooshes into the yellow circle -->
    <path class="swoosh-green" d="M0,342 C180,332 380,352 520,384 L520,398 C380,376 190,370 0,400 Z" fill="var(--brand-green)"/>
    <path class="swoosh-yellow" d="M0,442 C160,414 350,398 520,400 L520,408 C340,412 170,428 0,458 Z" fill="var(--brand-yellow)"/>
    <circle class="accent-circle" cx="549" cy="390" r="65" fill="var(--brand-yellow)"/>

    <!-- bottom waves -->
    <path class="wave-yellow" d="M470,1080 C620,990 820,948 1000,950 L1000,985 C820,980 650,1010 520,1070 Z" fill="var(--brand-yellow)"/>
    <path class="wave-green" d="M820,975 C900,975 960,1000 1000,1040 L1000,1080 C960,1030 900,1000 820,985 Z" fill="var(--brand-green)"/>
    <path class="wave-left-yellow" d="M0,1085 C40,1120 150,1140 300,1135 L300,1142 C150,1150 40,1135 0,1110 Z" fill="var(--brand-yellow)"/>
    <path class="wave-left-green" d="M0,1110 C60,1140 170,1158 300,1148 L300,1158 C170,1170 60,1160 0,1140 Z" fill="var(--brand-green)"/>
    <path class="wave-blue" d="M0,1140 C120,1175 300,1165 460,1085 C620,1005 820,985 1000,1000 L1000,1200 L0,1200 Z" fill="var(--sky-blue)"/>
  </svg>

  <header class="brand">
    <div class="brand-mark">
      <span class="brand-dot"></span>
      <span class="brand-acronym">YBSN</span>
    </div>
    <h1 class="brand-name">Young Balance Support<br>Network</h1>
  </header>

  <section class="intro">
    <h2 class="section-title">Vestibule ?</h2>
    <p>The vestibule is a little known sensory organ, the basis building block for equilibrium, a sixth sense hidden within the inner ear. This cavity bored within the bone of the base of the skull is truly a labyrinth sheltering both the auditory apparatus (or cochlea, shaped like a snail’s shell) and the vestibular apparatus (called the vestibule).</p>
  </section>

  <section class="consequences">
    <h2 class="section-title">Consequences that can be observed ?</h2>
    <ul>
      <li>Delay of postural control and of psychomotor development</li>
      <li>Delayed and uncertain walking, falling</li>
      <li>Discomfort for rapid movements</li>
      <li>Avoidance reactions</li>
      <li>A great expense of energy, easily fatigued, global lack of attention for learning, a feeling of doing two things at the same time</li>
      <li>Poor spatial representations</li>
    </ul>
  </section>

  <section class="compensation">
    <h2 class="section-title">Basic principles of<br>compensation ?</h2>
    <p>Without vestibular information the child, in order to maintain equilibrium, must strengthen two other sensory inputs:</p>
    <p>• vision, searching for fixed landmarks to stabilize gaze and body posture,</p>
    <p>• proprioception, seeking stable and secure points of support for the body.</p>
  </section>

  <div class="social">
    <span class="social-dot"></span>
    <span class="social-name">ybsnetwork</span>
  </div>

  <footer class="contact">
    <div>CCP: 27-530418-6</div>
    <div>info@ybsnetwork.org</div>
    <div class="web">www.ybsnetwork.org</div>
  </footer>
</main>
</body>
</html>
```